"Aviation Law Firm Needs Banner for Fly-In Website"

My firm is looking for a web banner which will be advertised on www.kestrel-meet.org. The banner is going to be used for advertisement leading up to the big fly-in event being held in April.

My law firm represents pilots, plane owners, airlines, and anyone else that has an interest in aviation.

I would like to see some animation if possible, which would include aviation/cutting edge themes.

I would like to incorporate my logo and background images from my website (attached).

The advertisement should discretely near the firm name say "Offices: Brookvale"

The advertised words should be "Vectoring You Through Legal Turbulence"

The advertisement should also include my telephone number: "1-855-ROW-4738" and also my website "www.TheCounselDesk.com"

The call to action should say "Contact The Counsel Desk"

This is a Vertical Ad and its dimensions are 300x600 PX (72 DPI)

Must be in PNG or JPEG format.

Target Market(s)

Pilots/Aviation Enthusiasts

Industry/Entity Type

Law Firm

Font styles to use
Serif
Sans Serif

Colors
fbf289
fbed22
ffffff
1b1b1b
000000

Requirements
Must have
• The banner should definitely look professional, yet cutting edge. The banner definitely needs those things listed in the project description.
Nice to have
• Animation

```html
<!DOCTYPE html>
<html lang="en">
<head>
<meta charset="utf-8">
<title>The Marlow Law Firm – Vertical Banner Frames</title>
<link rel="stylesheet" href="https://fonts.googleapis.com/css2?family=Arimo:wght@400;700&family=Cinzel:wght@400;600&display=swap">
<style>
  :root {
    --yellow: #fbed22;
    --pale-yellow: #fbf289;
    --white: #ffffff;
    --ink: #1b1b1b;
    --black: #000000;
    --phone-grey: #3a3a3a;
    --frame-line: #8a8a8a;
    --orange-top: #ffc34a;
    --orange-bottom: #f39200;
    --button-text: #6a3b00;
  }
  * { box-sizing: border-box; margin: 0; padding: 0; }
  html, body { width: 1200px; height: 1091px; overflow: hidden; background: var(--white); }
  body { position: relative; font-family: "Arimo", Arial, sans-serif; }

  .banner {
    position: absolute; top: 188px; width: 321px; height: 646px;
    border: 1px solid var(--frame-line); overflow: hidden; background: var(--black);
  }
  .banner--a { left: 105px; }
  .banner--b { left: 451px; }
  .banner--c { left: 798px; }

  .banner__photo {
    position: absolute; left: 0; top: 280px; width: 100%; height: 230px;
    background:
      radial-gradient(ellipse 40% 55% at 50% 50%, #e6e6e6 0%, #9a9a9a 35%, rgba(40,40,40,0) 70%),
      linear-gradient(180deg, #111 0%, #3a3a3a 45%, #6b6b6b 70%, #222 100%);
  }
  .banner__shapes { position: absolute; inset: 0; width: 100%; height: 100%; }

  .brand {
    position: absolute; top: 24px; left: 0; width: 100%; height: 50px;
  }
  .brand__mark {
    position: absolute; left: 26px; top: 6px; width: 30px; height: 30px;
    border-radius: 50%; background: var(--pale-yellow);
  }
  .brand__name {
    position: absolute; left: 92px; right: 12px; top: 4px; text-align: center;
    font-family: "Cinzel", Georgia, serif; font-weight: 400; font-size: 16px;
    color: var(--white); letter-spacing: 0.3px;
  }
  .brand__practice {
    position: absolute; left: 92px; right: 12px; top: 26px; text-align: center;
    font-family: "Cinzel", Georgia, serif; font-size: 9px; color: var(--white);
    display: flex; align-items: center; gap: 5px;
  }
  .brand__practice::before, .brand__practice::after {
    content: ""; flex: 1; height: 1px; background: var(--white);
  }

  .headline {
    position: absolute; left: 36px; right: 36px; top: 140px; height: 96px;
    display: flex; align-items: center; justify-content: center;
    text-align: center; font-weight: 700; text-transform: uppercase; line-height: 1.14;
  }
  .headline--yellow { color: var(--yellow); font-size: 24px; }
  .headline--white { color: var(--white); font-size: 19px; }
  .headline--pale { color: var(--pale-yellow); font-size: 21px; }

  .office {
    position: absolute; left: 0; width: 100%; top: 244px; text-align: center;
    color: var(--white); font-size: 16px; line-height: 20px;
  }

  .contact__phone {
    position: absolute; left: 0; width: 100%; top: 528px; text-align: center;
    color: var(--phone-grey); font-size: 24px; font-weight: 700; letter-spacing: 0.5px;
  }
  .contact__web {
    position: absolute; left: 0; width: 100%; top: 558px; text-align: center;
    color: var(--ink); font-size: 12px; font-weight: 700;
  }

  .cta {
    position: absolute; left: 24px; top: 590px; width: 259px; height: 42px;
    border-radius: 4px;
    background: linear-gradient(180deg, var(--orange-top) 0%, var(--orange-bottom) 100%);
    box-shadow: 0 4px 0 #9c5a00;
    display: flex; align-items: center; justify-content: center; gap: 10px;
    color: var(--button-text); font-size: 15px; font-weight: 700; text-decoration: none;
  }
  .cta__icon { width: 24px; height: 24px; }

  .frame-label {
    position: absolute; top: 866px; width: 321px; text-align: center;
    font-size: 17px; color: var(--ink); letter-spacing: 0.5px;
  }
  .frame-label--a { left: 105px; }
  .frame-label--b { left: 451px; }
  .frame-label--c { left: 798px; }
</style>
</head>
<body>

<section class="banner banner--a">
  <div class="banner__photo" role="img" aria-label="Black and white photo of a jet airliner on the runway at night, nose facing forward"></div>
  <svg class="banner__shapes" viewBox="0 0 321 646" aria-hidden="true">
    <defs>
      <linearGradient id="panelA" x1="0" y1="0" x2="0" y2="1">
        <stop offset="0" stop-color="#2c2c2c"/><stop offset="1" stop-color="#0a0a0a"/>
      </linearGradient>
      <linearGradient id="baseA" x1="0" y1="0" x2="0" y2="1">
        <stop offset="0" stop-color="#ffffff"/><stop offset="0.55" stop-color="#f2f2f2"/><stop offset="1" stop-color="#d8d8d8"/>
      </linearGradient>
    </defs>
    <rect x="0" y="0" width="321" height="110" fill="#000"/>
    <path d="M0 135 Q160 70 321 135 L321 285 L0 285 Z" fill="url(#panelA)"/>
    <path d="M0 135 Q160 70 321 135" fill="none" stroke="#fbed22" stroke-width="9"/>
    <polygon points="30,118 291,118 291,262 160,308 30,262" fill="#000" stroke="#fff" stroke-width="3.5"/>
    <path d="M0 440 Q160 540 321 440" fill="none" stroke="#fbed22" stroke-width="9"/>
    <path d="M0 452 Q160 548 321 452 L321 646 L0 646 Z" fill="url(#baseA)"/>
  </svg>
  <header class="brand">
    <span class="brand__mark"></span>
    <p class="brand__name">The Marlow Law Firm</p>
    <p class="brand__practice">Aviation Law | Drone Law</p>
  </header>
  <h2 class="headline headline--yellow">Vectoring you through legal turbulence</h2>
  <p class="office">Office: Brookvale</p>
  <p class="contact__phone">1 - 855 - ROW - 4738</p>
  <p class="contact__web">www.TheCounselDesk.com</p>
  <a class="cta" href="#">Contact The Counsel Desk
    <svg class="cta__icon" viewBox="0 0 24 24"><circle cx="12" cy="12" r="11" fill="#7a3d00"/><polygon points="9,7 18,12 9,17" fill="#fff"/></svg>
  </a>
</section>

<section class="banner banner--b">
  <div class="banner__photo" role="img" aria-label="Black and white photo of a jet airliner on the runway at night, nose facing forward"></div>
  <svg class="banner__shapes" viewBox="0 0 321 646" aria-hidden="true">
    <defs>
      <linearGradient id="panelB" x1="0" y1="0" x2="0" y2="1">
        <stop offset="0" stop-color="#2c2c2c"/><stop offset="1" stop-color="#0a0a0a"/>
      </linearGradient>
      <linearGradient id="baseB" x1="0" y1="0" x2="0" y2="1">
        <stop offset="0" stop-color="#ffffff"/><stop offset="0.55" stop-color="#f2f2f2"/><stop offset="1" stop-color="#d8d8d8"/>
      </linearGradient>
    </defs>
    <rect x="0" y="0" width="321" height="110" fill="#000"/>
    <path d="M0 135 Q160 70 321 135 L321 285 L0 285 Z" fill="url(#panelB)"/>
    <path d="M0 135 Q160 70 321 135" fill="none" stroke="#fbed22" stroke-width="9"/>
    <polygon points="30,118 291,118 291,262 160,308 30,262" fill="#000" stroke="#fff" stroke-width="3.5"/>
    <path d="M0 440 Q160 540 321 440" fill="none" stroke="#fbed22" stroke-width="9"/>
    <path d="M0 452 Q160 548 321 452 L321 646 L0 646 Z" fill="url(#baseB)"/>
  </svg>
  <header class="brand">
    <span class="brand__mark"></span>
    <p class="brand__name">The Marlow Law Firm</p>
    <p class="brand__practice">Aviation Law | Drone Law</p>
  </header>
  <h2 class="headline headline--white">The law firm<br>for pilots,<br>air plane owners,<br>airlines</h2>
  <p class="office">Office: Brookvale</p>
  <p class="contact__phone">1 - 855 - ROW - 4738</p>
  <p class="contact__web">www.TheCounselDesk.com</p>
  <a class="cta" href="#">Contact The Counsel Desk
    <svg class="cta__icon" viewBox="0 0 24 24"><circle cx="12" cy="12" r="11" fill="#7a3d00"/><polygon points="9,7 18,12 9,17" fill="#fff"/></svg>
  </a>
</section>

<section class="banner banner--c">
  <div class="banner__photo" role="img" aria-label="Black and white photo of a jet airliner on the runway at night, nose facing forward"></div>
  <svg class="banner__shapes" viewBox="0 0 321 646" aria-hidden="true">
    <defs>
      <linearGradient id="panelC" x1="0" y1="0" x2="0" y2="1">
        <stop offset="0" stop-color="#2c2c2c"/><stop offset="1" stop-color="#0a0a0a"/>
      </linearGradient>
      <linearGradient id="baseC" x1="0" y1="0" x2="0" y2="1">
        <stop offset="0" stop-color="#ffffff"/><stop offset="0.55" stop-color="#f2f2f2"/><stop offset="1" stop-color="#d8d8d8"/>
      </linearGradient>
    </defs>
    <rect x="0" y="0" width="321" height="110" fill="#000"/>
    <path d="M0 135 Q160 70 321 135 L321 285 L0 285 Z" fill="url(#panelC)"/>
    <path d="M0 135 Q160 70 321 135" fill="none" stroke="#fbed22" stroke-width="9"/>
    <polygon points="30,118 291,118 291,262 160,308 30,262" fill="#000" stroke="#fff" stroke-width="3.5"/>
    <path d="M0 440 Q160 540 321 440" fill="none" stroke="#fbed22" stroke-width="9"/>
    <path d="M0 452 Q160 548 321 452 L321 646 L0 646 Z" fill="url(#baseC)"/>
  </svg>
  <header class="brand">
    <span class="brand__mark"></span>
    <p class="brand__name">The Marlow Law Firm</p>
    <p class="brand__practice">Aviation Law | Drone Law</p>
  </header>
  <h2 class="headline headline--pale">Tenacity,<br>respect,<br>dedicated,<br>faith</h2>
  <p class="office">Office: Brookvale</p>
  <p class="contact__phone">1 - 855 - ROW - 4738</p>
  <p class="contact__web">www.TheCounselDesk.com</p>
  <a class="cta" href="#">Contact The Counsel Desk
    <svg class="cta__icon" viewBox="0 0 24 24"><circle cx="12" cy="12" r="11" fill="#7a3d00"/><polygon points="9,7 18,12 9,17" fill="#fff"/></svg>
  </a>
</section>

<p class="frame-label frame-label--a">FRAME A</p>
<p class="frame-label frame-label--b">FRAME B</p>
<p class="frame-label frame-label--c">FRAME C</p>

</body>
</html>
```